Lumo4Kart - a fintech company - business card

We need a business card design for our Payments Technology company in Sydney, Australia. We provide business with payment solutions expanding across EFTPOS machines, online payment gateways and mobile payment solutions. We would like to see designs that are clean, classy and professional.
Target Market(s)
Business professionals, executives, c-suite
Industry/Entity Type
Fintech
Contact Information for Business Card
Will be on 400gsm. Logo will most likely be spot gloss unless designer recommends otherwise.
Font styles to use
Sans Serif
Requirements
Must have
- We need our website (lumo4kart.com.au), email (contact@lumo4kart.com.au), mobile (0432 587 904) and direct phone number (02 6815 3927) to feature on the card along with our logo (attached) and the words "EFTPOS | ONLINE | MOBILE"
- Font = Roboto

```html
<!DOCTYPE html>
<html lang="en">
<head>
<meta charset="utf-8">
<title>Lumo4Kart – Business Card</title>
<link rel="stylesheet" href="https://fonts.googleapis.com/css2?family=Roboto:wght@500;700&display=swap">
<style>
  :root {
    --brand-blue: #165b8c;
    --text-blue: #1a5a8a;
    --band-white: #f8f8f8;
    --name-grey: #6b6b6b;
    --fold-shadow: #d2d2d2;
    --decor-grey: #f3f3f3;
    --card-white: #ffffff;
  }
  html, body {
    margin: 0;
    padding: 0;
    overflow: hidden;
    background: var(--card-white);
  }
  .card {
    position: relative;
    width: 1200px;
    height: 685px;
    overflow: hidden;
    background: var(--card-white);
    font-family: "Roboto", Arial, sans-serif;
  }
  .backdrop {
    position: absolute;
    inset: 0;
  }
  .brand-panel {
    position: absolute;
    left: 0;
    top: 0;
    width: 457px;
    height: 685px;
    background: var(--brand-blue);
  }
  .name-band {
    position: absolute;
    left: 0;
    top: 231px;
    width: 520px;
    height: 194px;
    background: var(--band-white);
  }
  .brand-lockup {
    position: absolute;
    left: 0;
    top: 231px;
    width: 457px;
    height: 194px;
    display: flex;
    align-items: center;
    justify-content: center;
    gap: 16px;
  }
  .brand-dot {
    width: 40px;
    height: 40px;
    border-radius: 50%;
    background: var(--brand-blue);
  }
  .brand-name {
    margin: 0;
    font-size: 42px;
    font-weight: 700;
    letter-spacing: 0.5px;
    color: var(--name-grey);
    text-transform: uppercase;
  }
  .contact-list {
    position: absolute;
    left: 0;
    top: 0;
    margin: 0;
    padding: 0;
    list-style: none;
  }
  .contact-item {
    position: absolute;
    left: 685px;
    height: 80px;
    display: flex;
    align-items: center;
    white-space: nowrap;
    font-size: 34px;
    font-weight: 500;
    color: var(--text-blue);
  }
  .contact-item.mobile { top: 134px; }
  .contact-item.phone  { top: 245px; }
  .contact-item.email  { top: 360px; }
  .contact-item.web    { top: 472px; }
</style>
</head>
<body>
<div class="card">
  <svg class="backdrop" width="1200" height="685" viewBox="0 0 1200 685" aria-hidden="true">
    <circle class="decor-circle" cx="860" cy="330" r="360" fill="var(--decor-grey)"/>
    <polygon class="fold-shadow" points="457,425 520,425 457,548" fill="var(--fold-shadow)"/>
    <line class="timeline" x1="606" y1="174" x2="606" y2="685" stroke="var(--brand-blue)" stroke-width="6"/>

    <g class="icon icon-mobile" transform="translate(606 174)">
      <circle r="40" fill="var(--brand-blue)"/>
      <rect x="-12" y="-23" width="24" height="44" rx="4" fill="none" stroke="#fff" stroke-width="3"/>
      <line x1="-8" y1="-16" x2="8" y2="-16" stroke="#fff" stroke-width="2"/>
      <line x1="-8" y1="12" x2="8" y2="12" stroke="#fff" stroke-width="2"/>
      <circle cy="16.5" r="2" fill="#fff"/>
    </g>

    <g class="icon icon-phone" transform="translate(606 285)">
      <circle r="40" fill="var(--brand-blue)"/>
      <path d="M-16 -20 l8 -4 l8 12 l-6 5 q4 10 14 15 l5 -6 l12 8 l-4 8 q-6 6 -16 2 q-20 -10 -27 -28 q-2 -8 6 -12 z" fill="#fff"/>
    </g>

    <g class="icon icon-email" transform="translate(606 400)">
      <circle r="40" fill="var(--brand-blue)"/>
      <rect x="-20" y="-13" width="40" height="27" fill="none" stroke="#fff" stroke-width="3"/>
      <polyline points="-20,-13 0,4 20,-13" fill="none" stroke="#fff" stroke-width="3"/>
      <line x1="-20" y1="14" x2="-6" y2="0" stroke="#fff" stroke-width="2"/>
      <line x1="20" y1="14" x2="6" y2="0" stroke="#fff" stroke-width="2"/>
    </g>

    <g class="icon icon-web" transform="translate(606 512)" fill="none" stroke="#fff" stroke-width="2.5">
      <circle r="40" fill="var(--brand-blue)" stroke="none"/>
      <circle r="21"/>
      <ellipse rx="9" ry="21"/>
      <line x1="0" y1="-21" x2="0" y2="21"/>
      <line x1="-21" y1="0" x2="21" y2="0"/>
      <line x1="-18" y1="-10" x2="18" y2="-10"/>
      <line x1="-18" y1="10" x2="18" y2="10"/>
    </g>
  </svg>

  <div class="brand-panel"></div>
  <div class="name-band"></div>
  <div class="brand-lockup">
    <span class="brand-dot"></span>
    <h1 class="brand-name">Lumo4Kart</h1>
  </div>

  <ul class="contact-list">
    <li class="contact-item mobile">0432 587 904</li>
    <li class="contact-item phone">02 6815 3927</li>
    <li class="contact-item email">contact@lumo4kart.com.au</li>
    <li class="contact-item web">lumo4kart.com.au</li>
  </ul>
</div>
</body>
</html>
```